Adwords Banner for unique handmade Jewelery

We need one Banner for our Jewelerys
in 4 sizes:
300x250px
336x280px
728x90px
160x600px

http://www.fenka-lauro.de/schmuck/2/

```html
<!DOCTYPE html>
<html lang="de">
<head>
<meta charset="utf-8">
<title>fenka lauro – Jewellery Banner Set</title>
<link rel="stylesheet" href="https://fonts.googleapis.com/css2?family=Cormorant+Garamond:ital,wght@0,400;1,400&display=swap">
<style>
  :root {
    --page: #ffffff;
    --board: #f3e4c6;
    --board-light: #f8eed8;
    --red-deep: #7a0710;
    --red: #b3121d;
    --red-bright: #cf1f29;
    --logo-grey: #d9d3d6;
    --logo-board: #8a6f79;
    --white: #ffffff;
    --pink: #e98aa2;
    --teal: #5cc3c8;
    --silver: #d8d8dc;
  }
  * { box-sizing: border-box; margin: 0; padding: 0; }
  html, body { width: 1200px; height: 1200px; overflow: hidden; background: var(--page); }
  body { position: relative; font-family: "Cormorant Garamond", Georgia, serif; }

  .board {
    position: absolute; left: 70px; top: 70px; width: 1060px; height: 1060px;
    background: radial-gradient(circle at 40% 40%, var(--board-light), var(--board));
  }
  .hero-photo {
    position: absolute; left: 70px; top: 150px; width: 420px; height: 250px;
    background: linear-gradient(100deg, var(--teal) 0%, #9fd8d6 20%, var(--board) 40%, var(--pink) 55%, var(--board) 80%);
    border-radius: 0 0 120px 0; opacity: .85;
  }
  .logo {
    position: absolute; display: flex; align-items: center; gap: .25em;
    font-weight: 400; white-space: nowrap; line-height: 1;
  }
  .logo .mark { width: .45em; height: .45em; border-radius: 50%; background: currentColor; opacity: .7; }
  .board-logo { left: 80px; top: 88px; font-size: 50px; color: var(--logo-board); }

  .banner {
    position: absolute; overflow: hidden; color: var(--white);
    background:
      repeating-linear-gradient(105deg, rgba(0,0,0,.07) 0 14px, rgba(255,255,255,.03) 14px 30px),
      radial-gradient(ellipse at 50% 45%, var(--red-bright), var(--red) 45%, var(--red-deep));
    box-shadow: 0 1px 3px rgba(0,0,0,.25);
  }
  .banner .logo { color: var(--logo-grey); }
  .photo { position: absolute; border-radius: 40%; }
  .photo-hearts { background: linear-gradient(110deg, transparent 10%, var(--teal) 35%, var(--pink) 70%, transparent 90%); }
  .photo-heart { background: radial-gradient(circle, var(--pink) 40%, rgba(233,138,162,0) 72%); }
  .photo-bracelet { background: linear-gradient(90deg, transparent, var(--teal) 20%, var(--silver) 50%, var(--teal) 80%, transparent); border-radius: 30px; opacity: .9; }
  .photo-ring { background: radial-gradient(circle at 40% 45%, var(--teal) 30%, var(--silver) 52%, rgba(216,216,220,0) 72%); }
  .photo-earrings { background: radial-gradient(ellipse, #f3c6d2 30%, #a9dede 50%, rgba(169,222,222,0) 72%); }

  .headline { position: absolute; font-style: italic; line-height: 1; white-space: nowrap; text-shadow: 0 1px 2px rgba(0,0,0,.35); }
  .headline .small { font-size: .55em; }
  .headline .sub { display: block; font-size: .5em; }

  .banner-medium { left: 484px; top: 224px; width: 320px; height: 268px; }
  .banner-medium .logo { left: 28px; top: 14px; font-size: 32px; }
  .banner-medium .photo-hearts { left: 120px; top: 105px; width: 200px; height: 150px; }
  .banner-medium .headline { left: 8px; top: 204px; font-size: 25px; line-height: 1.1; }

  .banner-sky { left: 818px; top: 224px; width: 172px; height: 642px; }
  .banner-sky .logo { left: 8px; top: 8px; font-size: 22px; }
  .banner-sky .photo-heart { left: 10px; top: 110px; width: 130px; height: 130px; }
  .banner-sky .photo-bracelet { left: 0; top: 290px; width: 172px; height: 50px; }
  .banner-sky .photo-ring { left: 8px; top: 385px; width: 164px; height: 175px; }
  .banner-sky .headline { right: 14px; top: 556px; font-size: 38px; text-align: right; }

  .banner-large { left: 445px; top: 566px; width: 360px; height: 300px; }
  .banner-large .logo { left: 14px; top: 12px; font-size: 34px; }
  .banner-large .photo-ring { left: 95px; top: 58px; width: 250px; height: 170px; }
  .banner-large .headline { right: 50px; top: 226px; font-size: 44px; text-align: right; }

  .banner-leader { left: 210px; top: 878px; width: 780px; height: 96px; }
  .banner-leader .logo { left: 22px; top: 20px; font-size: 34px; }
  .banner-leader .photo-earrings { left: 340px; top: 10px; width: 140px; height: 78px; }
  .banner-leader .headline { right: 26px; top: 14px; font-size: 40px; text-align: right; }
</style>
</head>
<body>
  <div class="board">
  </div>
  <div class="hero-photo" role="img" aria-label="Close-up of a silver chain with a turquoise and a pink glass heart bead"></div>
  <div class="logo board-logo"><span>fenka lauro</span><span class="mark"></span></div>

  <section class="banner banner-medium" aria-label="300 by 250 banner">
    <div class="logo"><span>fenka lauro</span><span class="mark"></span></div>
    <div class="photo photo-hearts" role="img" aria-label="Silver chain with turquoise and pink glass hearts"></div>
    <p class="headline">The Riches<br>&nbsp;&nbsp;&nbsp;Collection</p>
  </section>

  <section class="banner banner-sky" aria-label="160 by 600 banner">
    <div class="logo"><span>fenka lauro</span><span class="mark"></span></div>
    <div class="photo photo-heart" role="img" aria-label="Pink glass heart on a silver chain"></div>
    <div class="photo photo-bracelet" role="img" aria-label="Bracelet with turquoise glass beads"></div>
    <div class="photo photo-ring" role="img" aria-label="Silver ring with turquoise glass stone"></div>
    <p class="headline"><span class="small">The </span>Perfect<span class="sub">Collection</span></p>
  </section>

  <section class="banner banner-large" aria-label="336 by 280 banner">
    <div class="logo"><span>fenka lauro</span><span class="mark"></span></div>
    <div class="photo photo-ring" role="img" aria-label="Silver ring with turquoise glass stone"></div>
    <p class="headline"><span class="small">The </span>Perfect Fit<span class="sub">Collection</span></p>
  </section>

  <section class="banner banner-leader" aria-label="728 by 90 banner">
    <div class="logo"><span>fenka lauro</span><span class="mark"></span></div>
    <div class="photo photo-earrings" role="img" aria-label="Pair of pink and turquoise glass drop earrings"></div>
    <p class="headline"><span class="small">The </span>Perfect<span class="sub">Collection</span></p>
  </section>
</body>
</html>
```